Business card design for upmarket Home Technology design and Installation company

Hello designers, we need a great business card designed.
We need it to convey high tech, and also sophistication .
We work with some of the most affluent people in the world building them home technology systems, and A/V entertainment systems.

Services offered include the following:
Design, sales, installation, and maintenance of

*Home Automation systems
*Distributed / Multi-Room Audio and Video
*High Performance Networks & WiFi
* Lighting and Shade Control
*Home cinema
*Security and CCTV Systems

I have included a copy of our logo to use for your design efforts.

Target Market(s)

Upmarket clients with multi million euro villas.

Industry/Entity Type

Home technology

Contact Information for Business Card

NAME: Derek Halloran ADDRESS: Plaza Brisa Local 42, Port Andratx, 07392 PHONE: +34-602-518-794 EMAIL: DHalloran@VELTRAsmarthomes.com WEB: www.veltrasmarthomes.com

Requirements
Must have
• Our Logo, and our tagline

```html
<!DOCTYPE html>
<html lang="en">
<head>
<meta charset="utf-8">
<title>VELTRA Business Card</title>
<link href="https://fonts.googleapis.com/css2?family=Montserrat:wght@400;500;700&display=swap" rel="stylesheet">
<style>
  :root {
    --bg: #232323;
    --card: #050505;
    --gold: #e2c167;
    --gold-deep: #b98a2c;
    --gold-light: #f7e48a;
    --text: #f2f2f2;
    --grey: #555555;
  }
  * { margin: 0; padding: 0; box-sizing: border-box; }
  html, body { width: 1200px; height: 900px; overflow: hidden; }
  body {
    background: radial-gradient(ellipse at 50% 30%, #3a3a3a 0%, var(--bg) 55%, #111 100%);
    font-family: "Montserrat", sans-serif;
    position: relative;
  }
  .card {
    position: absolute;
    left: 250px;
    width: 700px;
    height: 400px;
    background: var(--card);
    box-shadow: 0 18px 40px rgba(0,0,0,0.6);
    overflow: hidden;
  }
  .card--back { top: 40px; }
  .card--front { top: 465px; }

  .brand-name {
    color: var(--gold);
    font-weight: 500;
    letter-spacing: 10px;
    position: absolute;
    white-space: nowrap;
  }
  .card--back .brand-name {
    font-size: 52px;
    left: 105px;
    top: 200px;
    transform: translate(-50%, -50%) rotate(-90deg);
    transform-origin: center;
  }
  .divider {
    position: absolute;
    width: 2px;
    background: var(--gold);
  }
  .card--back .divider { left: 190px; top: 70px; height: 260px; }

  .services {
    position: absolute;
    left: 225px;
    top: 82px;
    color: var(--text);
  }
  .services-title {
    color: var(--gold);
    font-weight: 700;
    font-size: 17px;
    margin-bottom: 8px;
  }
  .services-intro { font-size: 15px; margin-bottom: 6px; }
  .services-list { list-style: none; }
  .services-list li {
    font-size: 15px;
    line-height: 26px;
    display: flex;
    align-items: center;
    gap: 10px;
  }
  .bullet {
    width: 13px; height: 13px;
    border: 2px solid var(--gold);
    border-radius: 50%;
    flex: none;
  }

  .card--front .brand-name { font-size: 52px; left: 40px; top: 128px; }
  .card--front .divider { left: 340px; top: 105px; height: 225px; }
  .contact {
    position: absolute;
    left: 365px;
    top: 108px;
    color: var(--text);
    white-space: nowrap;
  }
  .contact-name {
    color: var(--gold);
    font-weight: 700;
    font-size: 22px;
    letter-spacing: 0.5px;
  }
  .contact-role { font-size: 18px; margin-bottom: 20px; }
  .contact-address { font-size: 17px; line-height: 24px; margin-bottom: 20px; }
  .contact-line {
    font-size: 16px;
    line-height: 26px;
    display: flex;
    align-items: center;
    gap: 8px;
  }
  .contact-line svg { width: 15px; height: 15px; flex: none; }
  .band { position: absolute; left: 0; bottom: 0; }
</style>
</head>
<body>

<section class="card card--back">
  <div class="brand-name">VELTRA</div>
  <div class="divider"></div>
  <div class="services">
    <p class="services-title">Services offered include the following:</p>
    <p class="services-intro">Design, sales, installation, and maintenance of</p>
    <ul class="services-list">
      <li><span class="bullet"></span>Home Automation systems</li>
      <li><span class="bullet"></span>Distributed / Multi-Room Audio and Video</li>
      <li><span class="bullet"></span>High Performance Networks &amp; WiFi</li>
      <li><span class="bullet"></span>Lighting and Shade Control</li>
      <li><span class="bullet"></span>Home cinema</li>
      <li><span class="bullet"></span>Security and CCTV Systems</li>
    </ul>
  </div>
</section>

<section class="card card--front">
  <div class="brand-name">VELTRA</div>
  <div class="divider"></div>
  <div class="contact">
    <p class="contact-name">DEREK HALLORAN</p>
    <p class="contact-role">Founder</p>
    <p class="contact-address">Plaza Brisa Local 42,<br>Port Andratx, 07392</p>
    <p class="contact-line">
      <svg viewBox="0 0 16 16"><path d="M3 2h3l1.5 3.5-2 1.2a8 8 0 0 0 3.8 3.8l1.2-2L14 10v3a1 1 0 0 1-1 1A11 11 0 0 1 2 3a1 1 0 0 1 1-1z" fill="#f2f2f2"/></svg>
      +34-602-518-794
    </p>
    <p class="contact-line">
      <svg viewBox="0 0 16 16"><rect x="1" y="3" width="14" height="10" fill="#f2f2f2"/><path d="M1 3l7 6 7-6" stroke="#050505" stroke-width="1.4" fill="none"/></svg>
      DHalloran@VELTRAsmarthomes.com
    </p>
    <p class="contact-line">
      <svg viewBox="0 0 16 16"><circle cx="8" cy="8" r="7" fill="#f2f2f2"/><path d="M1 8h14M8 1c-3 3.5-3 10.5 0 14M8 1c3 3.5 3 10.5 0 14" stroke="#050505" stroke-width="1" fill="none"/></svg>
      www.veltrasmarthomes.com
    </p>
  </div>
  <svg class="band" width="700" height="80" viewBox="0 0 700 80" aria-hidden="true">
    <defs>
      <linearGradient id="goldBand" x1="0" x2="1" y1="0" y2="0">
        <stop offset="0" stop-color="#b98a2c"/>
        <stop offset="0.5" stop-color="#f7e48a"/>
        <stop offset="1" stop-color="#b98a2c"/>
      </linearGradient>
    </defs>
    <polygon points="0,0 300,0 332,80 0,80" fill="url(#goldBand)"/>
    <polygon points="310,22 700,22 700,30 313,30" fill="#e2c167"/>
    <polygon points="318,42 700,42 700,80 334,80" fill="#555555"/>
  </svg>
</section>

</body>
</html>
```